Robotic startup business cards

We are looking for a design for a set of business cards which reflect the spirit and humor of Vortalo Robotics. We want to present ourselves as sleek, professional, but laid-back consulting company.

We primarily focus on developing robotic arms software. This software controls robots and does things like grab items, pick objects up, move them, etc.

We want to allow you maximum design creativity, but do ask that you consider our existing style guidelines (see attached files) in order to make our brand cohesive.

Target Market(s)

Startups and Mid-size robotic companies

Industry/Entity Type

Business

Contact Information for Business Card

Miro Halvensky, PhD
Roboticist | Vortalo Consulting | 318.570.9164

Font styles to use
Other font styles liked:
• Source code pro

Requirements
Must have
• robots or robotic arms
• similar color scheme that works with existing brand guidelines
Nice to have
• please consider our existing style guidelines (see attached files) in order to make our brand cohesive.
• minimalism style is generally nice.
Should not have
• An old, boring, or corporate feel. Too much text.

```html
<!DOCTYPE html>
<html lang="en">
<head>
<meta charset="utf-8">
<title>Vortalo Robotics — Business Cards</title>
<link href="https://fonts.googleapis.com/css2?family=Source+Code+Pro:wght@300;400;600;700&display=swap" rel="stylesheet">
<style>
  :root {
    --stage: #2a2724;
    --card-black: #050607;
    --mint: #4cc497;
    --white: #f2f4f5;
    --cyan: #2db4d6;
    --cyan-deep: #0d4f6b;
    --teal-glow: #1f8fa8;
    --amber: #ffa63a;
  }
  * { margin: 0; padding: 0; box-sizing: border-box; }
  html, body {
    width: 1200px; height: 784px; overflow: hidden;
    background: var(--stage);
    font-family: "Source Code Pro", monospace;
  }
  .canvas {
    width: 1200px; height: 784px;
    display: flex; align-items: center; justify-content: center; gap: 40px;
  }
  .card {
    position: relative;
    width: 560px; height: 320px;
    background: var(--card-black);
    border-radius: 4px;
    overflow: hidden;
    box-shadow: 0 18px 40px rgba(0,0,0,0.45);
  }
  .wordmark {
    position: absolute;
    display: flex; align-items: center; gap: 18px;
  }
  .wordmark-square {
    width: 42px; height: 42px;
    background: var(--mint);
    border-radius: 6px;
  }
  .wordmark-name {
    color: var(--white);
    font-weight: 300;
    font-size: 34px;
    letter-spacing: 0.18em;
  }

  /* Front card */
  .front-art {
    position: absolute; right: 0; top: 0;
    width: 430px; height: 230px;
    background:
      radial-gradient(circle at 62% 42%, rgba(80,220,240,0.85) 0%, rgba(45,180,214,0.55) 18%, rgba(13,79,107,0.55) 42%, rgba(5,6,7,0) 70%),
      radial-gradient(circle at 30% 60%, rgba(220,235,240,0.45) 0%, rgba(5,6,7,0) 35%),
      linear-gradient(160deg, #0a2d45 0%, #06324a 45%, var(--card-black) 100%);
  }
  .front .wordmark { left: 34px; top: 196px; }

  /* Back card */
  .back-art {
    position: absolute; right: 0; top: 0;
    width: 330px; height: 320px;
    background:
      radial-gradient(circle at 40% 20%, rgba(140,210,240,0.65) 0%, rgba(45,180,214,0.35) 25%, rgba(5,6,7,0) 60%),
      radial-gradient(circle at 20% 52%, rgba(255,166,58,0.55) 0%, rgba(255,166,58,0) 8%),
      radial-gradient(circle at 88% 55%, rgba(255,166,58,0.45) 0%, rgba(255,166,58,0) 7%),
      linear-gradient(180deg, #0e3550 0%, #0a2a3c 50%, #081a24 80%, var(--card-black) 100%);
    -webkit-mask-image: linear-gradient(90deg, transparent 0%, #000 30%);
    mask-image: linear-gradient(90deg, transparent 0%, #000 30%);
  }
  .back .wordmark { left: 34px; top: 34px; }
  .contact {
    position: absolute; left: 44px; top: 178px;
  }
  .contact-name {
    color: var(--mint);
    font-size: 22px; font-weight: 400;
    letter-spacing: 0.04em;
  }
  .contact-name .degree { font-size: 13px; }
  .contact-role, .contact-company {
    color: var(--white);
    font-size: 11px; font-weight: 700;
    letter-spacing: 0.06em;
    margin-left: 42px;
    line-height: 1.45;
  }
  .contact-role { margin-top: 2px; }
  .contact-phone {
    color: var(--white);
    font-size: 24px; font-weight: 600;
    letter-spacing: 0.02em;
    margin-top: 20px;
    margin-left: 42px;
  }
</style>
</head>
<body>
<main class="canvas">
  <section class="card front">
    <div class="front-art" role="img" aria-label="Illustration of a silver robotic arm reaching out in front of glowing cyan technology rings"></div>
    <div class="wordmark">
      <span class="wordmark-square"></span>
      <span class="wordmark-name">VORTALO</span>
    </div>
  </section>

  <section class="card back">
    <div class="back-art" role="img" aria-label="Illustration of a small robot placing a microchip onto a glowing circuit board"></div>
    <div class="wordmark">
      <span class="wordmark-square"></span>
      <span class="wordmark-name">VORTALO</span>
    </div>
    <div class="contact">
      <p class="contact-name">MIRO HALVENSKY,<span class="degree">PHD</span></p>
      <p class="contact-role">ROBOTICIST</p>
      <p class="contact-company">VORTALO CONSULTING</p>
      <p class="contact-phone">318.570.9164</p>
    </div>
  </section>
</main>
</body>
</html>
```